Verdane apparel business card

We are a clothing manufacturers agent based in London. Our clients are fashion retailers in the UK and Europe. We are looking for a business card design that communicates corporate stability and a creative edge

Target Market(s)

our customers are large international fashion retailers, smaller fashion stores and distributors and designers

Industry/Entity Type

Clothing

```html
<!DOCTYPE html>
<html lang="en">
<head>
<meta charset="utf-8">
<title>Verdane Apparel – Business Card</title>
<link rel="stylesheet" href="https://fonts.googleapis.com/css2?family=Arimo:wght@400;700&display=swap">
<style>
  :root {
    --backdrop: #e4e2de;
    --card: #ffffff;
    --ink: #2a2577;
    --band: #3a3589;
    --band-text: #ffffff;
  }
  html, body {
    margin: 0;
    padding: 0;
    width: 1200px;
    height: 885px;
    overflow: hidden;
    background: var(--backdrop);
  }
  .card {
    position: absolute;
    left: 150px;
    top: 182px;
    width: 900px;
    height: 520px;
    background: var(--card);
    border-radius: 22px;
    overflow: hidden;
    box-shadow: 0 6px 24px rgba(0,0,0,0.12);
    color: var(--ink);
  }
  .company-name {
    position: absolute;
    left: 70px;
    top: 66px;
    margin: 0;
    font-family: "Arimo", Arial, sans-serif;
    font-weight: 400;
    font-size: 54px;
    letter-spacing: 4px;
    text-transform: uppercase;
    white-space: nowrap;
  }
  .divider {
    position: absolute;
    left: 0;
    top: 0;
  }
  .person {
    position: absolute;
    left: 330px;
    top: 170px;
    font-family: "Arimo", Arial, sans-serif;
  }
  .person-name {
    margin: 0;
    font-weight: 700;
    font-size: 25px;
    letter-spacing: 0.5px;
  }
  .person-role {
    margin: 2px 0 0 70px;
    font-size: 15px;
  }
  .contact {
    position: absolute;
    left: 470px;
    top: 262px;
    margin: 0;
    padding: 0;
    list-style: none;
    font-family: "Arimo", Arial, sans-serif;
    font-size: 22px;
    line-height: 32px;
  }
  .address-band {
    position: absolute;
    left: 0;
    bottom: 0;
    width: 100%;
    height: 104px;
    background: var(--band);
    color: var(--band-text);
    font-family: "Arimo", Arial, sans-serif;
    font-size: 24px;
    display: flex;
    align-items: center;
    padding-left: 200px;
    box-sizing: border-box;
  }
</style>
</head>
<body>
  <article class="card">
    <h1 class="company-name">Verdane apparel</h1>
    <svg class="divider" width="900" height="416" viewBox="0 0 900 416" aria-hidden="true">
      <line x1="0" y1="190" x2="322" y2="190" stroke="#2a2577" stroke-width="2.5"/>
      <line x1="660" y1="190" x2="900" y2="190" stroke="#2a2577" stroke-width="2.5"/>
    </svg>
    <div class="person">
      <p class="person-name">EMPLOYEE NAME</p>
      <p class="person-role">Managing Director</p>
    </div>
    <ul class="contact">
      <li>0012 3456 789</li>
      <li>info@youremail.com</li>
      <li>www.yourwebsite.com</li>
    </ul>
    <footer class="address-band">Your Adress Inc 2nd Lane, Ave Elmford, NJ 00000</footer>
  </article>
</body>
</html>
```